Emergency and Referral Vet Hospital promotional sticker design

We're looking at getting some stickers designed that we could give to clients to put on their cars for promotion and advertising. If they could also be suitable for a goodie bag for conference too that would be great. I like the look of water-colour backgrounds, we'll need to include our logo and probably our address (Unit 4/372 Tarvenny Drive Success). We also have a hospital motto "... because they're family" if that could somehow be integrated, we only care for small animals (dogs, cats etc) but the design is very open to suggestion. Would love to see what you can create.

Industry/Entity Type

Veterinary

Colors
0054AA
0677BA
7BADD7
CADEEF
E8F1F8
0094D4
00A9DD
6FCCEA
C7EBF8
E9F6FB

Requirements
Nice to have
• Think beach vibes, blues maybe paw print shapes etc

```html
<!DOCTYPE html>
<html lang="en">
<head>
<meta charset="utf-8">
<title>Tidemark Vet Hospital – because they're family</title>
<link rel="stylesheet" href="https://fonts.googleapis.com/css2?family=Anton&family=Poppins:wght@600&display=swap">
<style>
  :root {
    --navy: #1b5895;
    --brand-blue: #0054aa;
    --mid-blue: #5f9bd3;
    --soft-blue: #7badd7;
    --pale-blue: #cadeef;
    --mist: #e8f1f8;
    --panel: #f4f5f7;
    --ink: #161616;
  }
  * { margin: 0; padding: 0; box-sizing: border-box; }
  html, body { width: 1200px; height: 800px; overflow: hidden; background: #fff; }
  .sticker { position: relative; width: 1200px; height: 800px; overflow: hidden; background: var(--panel); }

  .clinic-photo {
    position: absolute; left: 0; top: 0; width: 640px; height: 800px;
    background:
      linear-gradient(180deg, rgba(255,255,255,0) 60%, rgba(40,40,45,.35) 100%),
      linear-gradient(100deg, #cfd6db 0%, #e7e9ea 30%, #5d8ec4 48%, #e2c6a3 70%, #f1ece6 85%, #d8dde2 100%);
  }
  .glass-band {
    position: absolute; left: 557px; top: 0; width: 90px; height: 800px;
    background: rgba(123,173,215,.55);
    border-bottom-left-radius: 70px 180px;
  }
  .content-panel {
    position: absolute; left: 637px; top: 0; width: 563px; height: 800px;
    background: linear-gradient(135deg, #f7f8f9 0%, #eef0f2 100%);
    border-bottom-left-radius: 100px 170px;
  }

  .corner-circle { position: absolute; border-radius: 50%; }
  .corner-circle.top-ring { left: 1032px; top: -110px; width: 290px; height: 280px; background: #e6e8ea; }
  .corner-circle.top-disc { left: 1054px; top: -100px; width: 250px; height: 245px; background: var(--mid-blue); }
  .corner-circle.bottom-ring { left: -95px; top: 572px; width: 360px; height: 360px; background: rgba(235,238,240,.7); }
  .corner-circle.bottom-disc { left: -70px; top: 608px; width: 310px; height: 310px; background: var(--mid-blue); }

  .paw { position: absolute; width: 80px; height: 82px; }
  .paw.one { left: 655px; top: 20px; }
  .paw.two { left: 1050px; top: 75px; }
  .paw.three { left: 657px; top: 305px; }
  .paw.four { left: 1053px; top: 515px; }

  .brand {
    position: absolute; left: 637px; width: 563px; top: 200px;
    display: flex; justify-content: center; align-items: center; gap: 10px;
    font-family: "Poppins", sans-serif; font-weight: 600; font-size: 27px; color: var(--ink);
  }
  .brand-dot { width: 16px; height: 16px; border-radius: 50%; background: var(--brand-blue); }

  .motto {
    position: absolute; left: 700px; width: 430px; top: 318px;
    font-family: "Anton", sans-serif; color: var(--navy);
    font-size: 62px; line-height: 78px; text-align: center; letter-spacing: .5px;
  }
  .motto span { display: block; }

  .location { position: absolute; left: 637px; width: 563px; top: 598px; text-align: center; }
  .location svg { width: 44px; height: 62px; display: block; margin: 0 auto 6px; }
  .address { font-family: "Poppins", sans-serif; font-weight: 600; font-size: 26px; color: var(--ink); }
</style>
</head>
<body>
<main class="sticker">
  <div class="clinic-photo" role="img" aria-label="Vet in blue scrubs and white coat examining a smiling corgi on a clinic table"></div>
  <div class="glass-band"></div>
  <div class="content-panel"></div>

  <div class="corner-circle top-ring"></div>
  <div class="corner-circle top-disc"></div>
  <div class="corner-circle bottom-ring"></div>
  <div class="corner-circle bottom-disc"></div>

  <div class="paw one" role="img" aria-label="Blue paw print"><svg viewBox="0 0 80 82"><ellipse cx="44" cy="58" rx="24" ry="20" fill="var(--soft-blue)"/></svg></div>
  <div class="paw two" role="img" aria-label="Blue paw print"><svg viewBox="0 0 80 82"><ellipse cx="30" cy="52" rx="22" ry="22" fill="var(--soft-blue)"/></svg></div>
  <div class="paw three" role="img" aria-label="Blue paw print"><svg viewBox="0 0 80 82"><ellipse cx="44" cy="58" rx="24" ry="20" fill="var(--soft-blue)"/></svg></div>
  <div class="paw four" role="img" aria-label="Blue paw print"><svg viewBox="0 0 80 82"><ellipse cx="36" cy="50" rx="24" ry="22" fill="var(--soft-blue)"/></svg></div>

  <div class="brand"><span class="brand-dot"></span><span class="brand-name">Tidemark</span></div>

  <h1 class="motto"><span>because</span><span>they're family</span></h1>

  <div class="location">
    <svg viewBox="0 0 44 62" aria-hidden="true">
      <path d="M22 0C10 0 0 9.6 0 21.5 0 37 22 62 22 62s22-25 22-40.5C44 9.6 34 0 22 0z" fill="var(--brand-blue)"/>
      <circle cx="22" cy="21" r="7" fill="#fff"/>
    </svg>
    <p class="address">Unit 4/372 Tarvenny Drive Success</p>
  </div>
</main>
</body>
</html>
```